Recruitment #1

We are looking for an effective ad to recruit work from home Loan Officers for our Mortgage Brokerage.
Use the following text...
Earn Mortgage Income in your sleep. Its as easy as 1, 2, 3.....
1) Solicit Potential Applicants (Word of Mouth, Email, Social Media etc.)
2) Take Complete Applications & Submit Them
3) Wait to Get Paid.......(Avg. $2,500 per closing)
"You open the Bluegate, We'll handle the rest"
No Experience Necessary
No Goals or Quotas
No Office Hours / Work from Home Office
...and We Fully Reimburse ALL LICENSING FEES!!
Email Resume to mkowal@bluegatehomeloans.com
Bluegate Financial Services, Inc.
731 W Orchard Avenue, #318
Baltimore, MD 21417
NMLS #386147
www.bluegatehomeloans.com
Phone (800) 640-2915
Licensed Mortgage Broker in MD and DC since 1997
Professionals looking to earn part time income at Loan Officers, preferably with strong social media following.
Loan

```html
<!DOCTYPE html>
<html lang="en">
<head>
<meta charset="utf-8">
<title>Bluegate Financial Services – Loan Officer Recruitment</title>
<link rel="stylesheet" href="https://fonts.googleapis.com/css2?family=Montserrat:wght@700;800&family=Roboto:ital,wght@0,300;0,400;0,700;1,400&display=swap">
<style>
  :root {
    --blue: #0a5aa8;
    --blue-deep: #084a8e;
    --yellow: #fff200;
    --gold: #a8954a;
    --white: #ffffff;
    --ink: #1b1b1b;
    --frame-line: #9ec0e4;
    --page-bg: #e9e9ee;
  }
  * { margin: 0; padding: 0; box-sizing: border-box; }
  html, body { width: 969px; height: 1200px; overflow: hidden; }
  body { background: var(--page-bg); font-family: "Roboto", Arial, sans-serif; position: relative; }

  .flyer {
    position: absolute; left: 78px; top: 36px;
    width: 625px; height: 868px;
    background: var(--white);
    transform: scale(1.3); transform-origin: 0 0;
    overflow: hidden;
  }
  .header-shape { position: absolute; left: 0; top: 0; width: 625px; height: 360px; }

  .headline__earn, .headline__income, .headline__sleep {
    position: absolute; left: 0; width: 625px; text-align: center; line-height: 1; white-space: nowrap;
  }
  .headline__earn {
    top: 36px;
    font-family: "Montserrat", Arial, sans-serif; font-weight: 800;
    font-size: 136px; color: var(--yellow);
    transform: scaleX(0.88); transform-origin: 50% 0;
  }
  .headline__income {
    top: 170px;
    font-family: "Montserrat", Arial, sans-serif; font-weight: 700;
    font-size: 41px; color: var(--white);
  }
  .headline__sleep {
    top: 214px;
    font-family: "Roboto", Arial, sans-serif; font-weight: 300;
    font-size: 42px; color: var(--yellow);
  }
  .ribbon-text {
    position: absolute; left: 140px; top: 287px; width: 348px; text-align: center;
    color: var(--white); font-size: 23px; font-weight: 300;
  }

  .photo {
    position: absolute; left: 320px; top: 352px; width: 305px; height: 398px;
    background: radial-gradient(ellipse at 55% 40%, #c98f72 0%, #8a5a45 35%, #f4f1ec 75%);
  }

  .steps { position: absolute; left: 53px; top: 376px; width: 300px; list-style: none; font-size: 14px; color: var(--ink); line-height: 1.3; }
  .steps li { margin-bottom: 10px; padding-left: 15px; text-indent: -15px; }

  .quote { position: absolute; left: 53px; top: 494px; width: 290px; color: var(--blue); }
  .quote__text { font-style: italic; font-size: 18px; line-height: 1.3; text-transform: uppercase; padding-left: 38px; }
  .quote__mark { position: absolute; font-family: Georgia, serif; font-size: 54px; font-weight: 700; line-height: 1; color: var(--blue); }
  .quote__mark--open { left: 0; top: -8px; }
  .quote__mark--close { left: 270px; top: 20px; }

  .perks { position: absolute; left: 53px; top: 570px; list-style: none; font-size: 14px; color: var(--ink); line-height: 1.3; }
  .perks li::before { content: "• "; }

  .reimburse { position: absolute; left: 53px; top: 636px; font-size: 14px; color: var(--ink); line-height: 1.3; }
  .reimburse strong { color: var(--blue); font-weight: 700; }

  .apply { position: absolute; left: 53px; top: 692px; border-left: 2px solid var(--blue); padding-left: 8px; font-size: 14px; line-height: 1.3; color: var(--ink); }

  .footer { position: absolute; left: 0; top: 750px; width: 625px; height: 118px; background: var(--blue); border-top: 4px solid var(--gold); }
  .footer__info { position: absolute; left: 53px; top: 22px; color: var(--white); font-size: 11px; line-height: 1.5; }
  .footer__name { font-weight: 700; font-size: 11.5px; }
  .footer__web { font-weight: 700; font-size: 11px; }
  .footer__note { font-size: 9px; opacity: 0.8; margin-top: 2px; }
  .social-badge { position: absolute; left: 354px; top: 58px; width: 61px; height: 22px; background: var(--white); border: 1px solid #cfd6e6; }
  .brand-box {
    position: absolute; left: 460px; top: 4px; width: 112px; height: 90px; background: var(--white);
    display: flex; align-items: center; justify-content: center; text-align: center;
    color: var(--blue); font-size: 12px; font-weight: 700; line-height: 1.2; padding: 6px;
  }
</style>
</head>
<body>
  <article class="flyer">
    <svg class="header-shape" viewBox="0 0 625 360" aria-hidden="true">
      <polygon points="0,0 625,0 625,272 312,346 0,272" fill="var(--blue)"/>
      <polygon points="0,272 312,346 625,272 625,282 312,356 0,282" fill="var(--gold)"/>
      <polygon points="0,262 312,336 625,262 625,272 312,346 0,272" fill="var(--blue-deep)"/>
      <path d="M12,264 V14 H613 V264" fill="none" stroke="var(--frame-line)" stroke-width="1"/>
      <polygon points="150,282 478,282 488,300 478,318 150,318 140,300" fill="var(--gold)"/>
    </svg>

    <header class="headline">
      <div class="headline__earn">EARN</div>
      <div class="headline__income">MORTGAGE INCOME</div>
      <div class="headline__sleep">IN YOUR SLEEP</div>
    </header>
    <div class="ribbon-text">Its as easy as 1, 2, 3.....</div>

    <div class="photo" role="img" aria-label="Photo of a smiling woman holding a fan of dollar bills"></div>

    <ol class="steps">
      <li>1) Solicit Potential Applicants (Word of Mouth, Email, Social Media etc.)</li>
      <li>2) Take Complete Applications &amp; Submit Them</li>
      <li>3) Wait to Get Paid.......(Avg. $2,500 per closing)</li>
    </ol>

    <blockquote class="quote">
      <span class="quote__mark quote__mark--open">“</span>
      <p class="quote__text">You open the Bluegate,<br>We'll handle the rest</p>
      <span class="quote__mark quote__mark--close">”</span>
    </blockquote>

    <ul class="perks">
      <li>No Experience Necessary</li>
      <li>No Goals or Quotas</li>
      <li>No Office Hours / Work from Home Office</li>
    </ul>

    <p class="reimburse">...and We Fully Reimburse<br><strong>ALL LICENSING FEES!!</strong></p>

    <p class="apply">Email Resume to<br>mkowal@bluegatehomeloans.com</p>

    <footer class="footer">
      <div class="footer__info">
        <div class="footer__name">BLUEGATE FINANCIAL SERVICES, INC.</div>
        <div>731 W Orchard Avenue, #318 Baltimore, MD 21417</div>
        <div>NMLS #386147</div>
        <div class="footer__web">www.bluegatehomeloans.com &nbsp;|&nbsp; Phone (800) 640-2915</div>
        <div class="footer__note">Licensed Mortgage Broker in MD and DC since 1997</div>
      </div>
      <div class="social-badge" aria-hidden="true"></div>
      <div class="brand-box">Bluegate Financial Services, Inc.</div>
    </footer>
  </article>
</body>
</html>
```